International Property Consultancy

Detailed Wireframe and info document attached.

Brief Overview:

I need a dynamic and well designed website that is easy to use and understand. It has to be unique and different to generic templates that most websites seem to be these days. PLEASE NO GENERIC TEMPLATES FROM THE INTERNET.

Our business has 10 years experience working on struggling international developments that we then work in-house for to turn around and brings bout success. We stay within a project often for long periods of time until success is achieved. We are unique in our approach and completely different to the standard routes to market for many developments. The site is for developers to see what we have done in regards to previous projects, as such we want to incorporate video into this site with a strong design aesthetic. There will be videos of the past projects we have worked on, which will act as case studies.

I like very simple but punchy websites, that people can navigate and understand very easily. Also a big fan of unique and well thought out design aesthetic.

Initial Site layout thoughts:

1) Homepage:
2) About Us
3) What we've done / Work
This part has the projects we have worked on (France, Portugal, London, Morocco). Each one will have some video content and photo images, but also would be good to have a succinct way to mention what we did and the successes in a clever and punchy way.

4) Contact Us

* This is just a guideline. Would be open to input and creative direction on your own part.

*More details and websites we like can be seen in the brief doc attached.

PLEASE VIEW THE WIREFRAME WORD DOC ATTACHED.

Here there are also some more examples to help:

Here are just a few examples of websites and what I like about them:

- www.velmorit.com (clean, nice geometric design aesthetic, good animation when loading and changing pages well thought out all though also coulee be considered a bit dull and basic after the initial homepage slide)
- https://www.farbridgeloop.net (Clean site, quite clinical, lacks video content and doesn't engage greatly).
- https://quiltmarsh.com (minimal, and like how it mixes the design aesthetic more with video and photo content)

- https://www.theamberotter.com (like the layout of this and how it displays the projects and work section)

- https://drov.com (Good use of video content)

- https://crafthalo.studio (minimal to the point and mixes design with video and animation etc...)

Here is another couple of cool websites that may help give you some direction: https://tidewellgroup.com www.drov.com

Hi there, One of the things I thought would be good on the homepage is to add the logo with a 'digital landscape' before flicking down into a slide with video content of the projects... Just an idea but have posted some pics in the brief. We would get this animated for the site. But if you have better ideas, please do run with them. Thanks,

Target Market(s)

Property developers

Number of Pages Required

4 page

Font styles to use
Other font styles liked:
• Read brief

Requirements
Must have
• Needs to be clean, dynamic and easy to follow on desktop and mobile. We will use it as a kind of portfolio website so will need to embed video of past projects we have worked on.

Read brief in docs.
Nice to have
• Clean
Should not have
• Not be another generic template website.
Not have random property stock photos. (We are not a property agency).

```html
<!DOCTYPE html>
<html lang="en">
<head>
<meta charset="utf-8">
<title>ostrelan — International Property Consultancy</title>
<link rel="stylesheet" href="https://fonts.googleapis.com/css2?family=Comfortaa:wght@400;700&family=Quicksand:wght@400;500;600&display=swap">
<style>
:root{
  --ink:#1b4a5c;
  --ink-dark:#1d4557;
  --blush:#f8e0da;
  --blush-text:#f6ddd6;
  --white:#ffffff;
  --body:#3f4f57;
  --line:#c9d6db;
}
*{box-sizing:border-box;margin:0;padding:0}
html,body{width:1200px;height:2418px;overflow:hidden;background:var(--white)}
body{font-family:"Quicksand",sans-serif;color:var(--body);position:relative}
.abs{position:absolute}
.brand{font-family:"Comfortaa",sans-serif;font-weight:700;letter-spacing:1px}

/* hero */
.hero{left:0;top:0;width:1200px;height:584px;background:linear-gradient(160deg,#5d86c4 0%,#4f77b6 45%,#2f4f7c 100%)}
.hero-logo{left:63px;top:20px;color:var(--white);font-size:38px}
.nav{right:200px;top:40px;display:flex;gap:52px;font-size:16px;color:var(--white)}
.social-top{right:63px;top:40px;display:flex;gap:8px}
.sq{width:18px;height:18px;background:var(--white);border-radius:3px}
.welcome{left:0;width:1200px;top:210px;text-align:center;font-family:"Comfortaa",sans-serif;font-weight:700;font-size:62px;color:var(--blush-text)}
.hero-name{left:0;width:1200px;top:290px;text-align:center;color:var(--white);font-size:84px}

/* about */
.about-media{left:474px;top:672px;width:726px;height:446px;background:linear-gradient(135deg,#e9e6e1 0%,#cfc5b8 45%,#a47a55 100%)}
.play{left:320px;top:180px}
.about-card{left:0;top:718px;width:605px;height:353px;background:var(--white);box-shadow:0 2px 14px rgba(0,0,0,.12);padding:14px 63px}
.h-section{font-family:"Comfortaa",sans-serif;font-weight:700;color:var(--ink);font-size:42px}
.about-card p{font-size:13.6px;line-height:21px;margin-top:14px;color:var(--body)}
.about-card p+p{margin-top:21px}
.btn-outline{display:inline-block;margin-top:12px;border:3px solid var(--ink);color:var(--ink);font-size:15px;padding:9px 16px;letter-spacing:.5px}

/* projects */
.projects{left:0;top:1204px;width:1200px;height:396px;background:var(--blush)}
.projects-title{left:87px;top:26px;line-height:54px}
.proj-img{top:61px;width:292px;height:275px;border-radius:4px}
.proj-1{left:334px;background:linear-gradient(180deg,#6b8fb2 0%,#d9d8d3 45%,#5d6f84 100%)}
.proj-2{left:754px;background:linear-gradient(160deg,#3c78d8 0%,#1f5fd0 60%,#3a84e0 100%)}
.proj-label{font-family:"Comfortaa",sans-serif;font-weight:700;font-size:29px;color:var(--ink);line-height:37px;top:222px}
.next{left:1083px;top:337px}

/* contact */
.contact-title{left:0;width:1200px;top:1682px;text-align:center}
.touch{left:188px;top:1756px;font-family:"Comfortaa",sans-serif;font-size:30px;color:var(--ink)}
.touch em{font-style:italic;font-weight:700}
.info{left:188px;font-size:15px;color:var(--body);line-height:21px}
.social-contact{left:188px;top:1955px;display:flex;gap:12px}
.social-contact .sq{width:27px;height:27px;background:var(--ink)}
.field{left:573px;width:438px;border:2px solid var(--ink);border-radius:3px;font-size:15px;color:#6d7a80;padding:11px 12px}
.btn-solid{left:858px;top:2008px;width:153px;height:44px;background:var(--ink);color:var(--white);font-size:16px;display:flex;align-items:center;justify-content:center;border-radius:2px}

/* footer */
.footer{left:0;top:2140px;width:1200px;height:278px;background:var(--ink-dark);color:var(--white)}
.foot-logo{left:98px;top:28px;font-size:46px;color:var(--blush-text)}
.foot-about{left:80px;top:106px;width:280px;text-align:center;font-size:13px;line-height:21px}
.foot-h{font-size:17px;color:var(--blush-text);top:34px}
.foot-list{font-size:13px;line-height:34px}
.news{left:850px;top:71px;width:263px;height:44px;background:var(--white);display:flex}
.news span{flex:1;font-size:13px;color:#6d7a80;padding:14px}
.news i{width:46px;background:var(--blush);display:flex;align-items:center;justify-content:center}
.social-foot{left:921px;top:145px;display:flex;gap:14px}
.social-foot .sq{width:31px;height:31px;background:var(--blush-text)}
.divider{left:86px;top:228px;width:1026px;height:1px;background:var(--line)}
.copy{left:0;width:1200px;top:247px;text-align:center;font-size:12.5px}
</style>
</head>
<body>

<section class="abs hero" role="img" aria-label="Upward view of a curved glass tower against a blue sky"></section>
<div class="abs brand hero-logo">ostrelan.</div>
<nav class="abs nav"><span>Home</span><span>About Us</span><span>Projects</span><span>Contact Us</span></nav>
<div class="abs social-top"><i class="sq"></i><i class="sq"></i><i class="sq"></i></div>
<h1 class="abs welcome">Welcome For</h1>
<div class="abs brand hero-name">ostrelan.</div>

<div class="abs about-media" role="img" aria-label="Video still of a bright open-plan living room and kitchen">
  <svg class="abs play" width="86" height="86" viewBox="0 0 86 86"><circle cx="43" cy="43" r="43" fill="rgba(40,40,40,.75)"/><path d="M34 27 L60 43 L34 59 Z" fill="#fff"/></svg>
</div>
<section class="abs about-card">
  <h2 class="h-section">About Us</h2>
  <p>Lorem ipsum dolor sit amet, consectetur adipisicing elit, sed do eiusmod tempor incididunt ut labore et dolore magna aliqua. Ut enim ad minim veniam, quis nostrud exercitation ullamco laboris nisi aliquip commodo consequat. Duis aute irure dolor in reprehenderit in voluptate velit esse cillum dolore eu fugiat nulla pariatur.</p>
  <p>Excepteur sint occaecat cupidatat non proident, sunt in culpa qui officia deserunt mollit anim id est laborum. Sed ut perspiciatis unde omnis iste natus error sit voluptatem accusantium doloremque laudantium, totam rem aperiam, eaque ipsa quae ab illo inventore veritatis</p>
  <span class="btn-outline">READ MORE</span>
</section>

<section class="abs projects">
  <h2 class="abs h-section projects-title">Our<br>Projects</h2>
  <div class="abs proj-img proj-1" role="img" aria-label="Portugal resort with white terraces above a pool"></div>
  <div class="abs proj-img proj-2" role="img" aria-label="Blue-washed street with steps in Morocco"></div>
  <div class="abs proj-label" style="left:290px">Portugal<br>Resort</div>
  <div class="abs proj-label" style="left:695px">Morocco</div>
  <svg class="abs next" width="30" height="26" viewBox="0 0 30 26"><path d="M2 13 H26 M16 3 L26 13 L16 23" stroke="#111" stroke-width="3.5" fill="none" stroke-linecap="round" stroke-linejoin="round"/></svg>
</section>

<h2 class="abs h-section contact-title">Contact Us</h2>
<div class="abs touch"><em>Get in</em> TOUCH</div>
<div class="abs info" style="top:1810px">Lykou 14 Str. 16452, Marenti<br>Athens,Greece</div>
<div class="abs info" style="top:1874px">+30-6900112233</div>
<div class="abs info" style="top:1916px">info@ ostrelan.com</div>
<div class="abs social-contact"><i class="sq"></i><i class="sq"></i><i class="sq"></i></div>
<div class="abs field" style="top:1764px;height:43px">Name</div>
<div class="abs field" style="top:1824px;height:43px">Email</div>
<div class="abs field" style="top:1884px;height:108px">Message</div>
<div class="abs btn-solid">SEND MESSAGE</div>

<footer class="abs footer">
  <div class="abs brand foot-logo">ostrelan.</div>
  <p class="abs foot-about">Lorem ipsum dolor sit amet, consectetur adipisicing elit, sed do eiusmod tempor incididunt ut labore et dolore magna aliqua.</p>
  <div class="abs foot-h" style="left:430px">Quike Links</div>
  <div class="abs foot-list" style="left:430px;top:60px">Home<br>About Us<br>Projects<br>Contact Us</div>
  <div class="abs foot-h" style="left:604px">Contact Us</div>
  <div class="abs" style="left:604px;top:78px;font-size:13px;line-height:17px">Lykou 14 Str. 16452, Marenti<br>Athens,Greece</div>
  <div class="abs" style="left:604px;top:130px;font-size:13px">+30-6900112233</div>
  <div class="abs" style="left:604px;top:164px;font-size:13px">info@ ostrelan.com</div>
  <div class="abs foot-h" style="left:850px">News Letter</div>
  <div class="abs news"><span>Enter Your Email</span><i><svg width="24" height="24" viewBox="0 0 24 24"><circle cx="10" cy="10" r="7" stroke="#1d4557" stroke-width="3" fill="none"/><path d="M15 15 L22 22" stroke="#1d4557" stroke-width="3.5" stroke-linecap="round"/></svg></i></div>
  <div class="abs social-foot"><i class="sq"></i><i class="sq"></i><i class="sq"></i></div>
  <div class="abs divider"></div>
  <div class="abs copy">© 2020 ostrelan. All rights reserved.</div>
</footer>

</body>
</html>
```